Tri Fold Brochure for Larkmoor Financial Planning SA

We need a tri fold and PDF (emailable) brochure for financial planning business located in a rural location in South Australia. I have attached the information we would like included. I would like the brochure to have a blue theme, as this is our corporate colour. I'm looking for something corporate, but not boring. It needs to catch the eye and engage our prospective clients. We have had some structural changes in the business and would like to portray a new company image that means business but is fresh and vibrant, yet very professional. It is possible that we could use the successful bid as a basis for our new website and further stationery needs.

Target Market(s)

Potential financial planning clients. We have a broad market 18-35 wealth accumulators, 35-50 wealth builders, 50-60 Pre-retirement, 60-75 retirement, 75+ Aged Care.

Industry/Entity Type

Financial Planning

Font styles to use
Sans Serif
Other font styles liked:
• Arial, verdana

Colors
0255a3
3176b5
85acd3
cfdeed
eaf1f7
ffffff
33a6d7
0392cd
85cae6

Requirements
Must have
• The Brevanta logo (which is in the uploaded material and cannot be changed), this needs to be placed close to the words as shown in the uploaded material. Our business logo. All the written information that I have attached less any design attributes I have attached. Some relatable photgraphs or images.
Nice to have
• The words "Certainty, Direction, and Peace of Mind" maybe in the back ground somewhere, sort of like a water mark. Any blue scheme is fine, with black and white included, take note of the version of blue in our logo. The fonts I have chosen can be used singularly or in a mixed format.
Should not have
• Photographs or designs used by other financial planning firms. Red, this is too confrontational.

```html
<!DOCTYPE html>
<html lang="en">
<head>
<meta charset="utf-8">
<title>Larkmoor Financial Planning SA – Brochure Spread</title>
<link rel="stylesheet" href="https://fonts.googleapis.com/css2?family=Arimo:wght@400;700&display=swap">
<style>
  :root {
    --page-bg: #6a6f7c;
    --brand-blue: #2c6499;
    --brand-blue-deep: #27588b;
    --heading-blue: #1f5fa0;
    --accent-blue: #3176b5;
    --ink: #111111;
    --paper: #fbfafb;
    --white: #ffffff;
    --watermark: #27568a;
  }
  * { box-sizing: border-box; margin: 0; padding: 0; }
  html, body { width: 1200px; height: 1200px; overflow: hidden; }
  body {
    background: var(--page-bg);
    font-family: "Arimo", Arial, sans-serif;
    position: relative;
  }
  .spread {
    position: absolute; left: 34px; top: 200px;
    width: 1132px; height: 800px;
    background: var(--brand-blue);
  }
  .rule { position: absolute; background: var(--white); }
  .rule--vertical { left: 365px; top: 0; width: 2px; height: 800px; }
  .rule--horizontal { left: 0; top: 476px; width: 1132px; height: 2px; }

  .panel { position: absolute; background: var(--paper); }
  .panel--what { left: 0; top: 0; width: 358px; height: 466px; }
  .panel--help { left: 0; top: 486px; width: 358px; height: 314px; }

  .heading {
    position: absolute; left: 39px;
    color: var(--heading-blue); font-weight: 700;
    letter-spacing: 0.2px;
  }
  .heading--lg { font-size: 25px; }
  .heading--md { font-size: 20px; }
  .body-copy {
    position: absolute; left: 39px; width: 290px;
    font-size: 13px; line-height: 16px; color: var(--ink);
  }
  .bullet-list { list-style: none; }
  .bullet-list li { padding-left: 9px; text-indent: -9px; }
  .bullet-list li::before { content: "•"; color: var(--accent-blue); margin-right: 3px; }

  .brand-mark {
    position: absolute; left: 64px; top: 160px; width: 230px;
    display: flex; align-items: center; gap: 10px;
    font-size: 17px; font-weight: 700; line-height: 21px;
    color: var(--heading-blue);
  }
  .brand-mark .square {
    flex: none; width: 26px; height: 26px; background: var(--heading-blue);
  }

  .tagline {
    position: absolute; left: 39px; top: 265px;
    font-size: 13px; line-height: 16px; font-weight: 700;
    color: var(--heading-blue);
  }

  .questions {
    position: absolute; left: 416px; top: 92px; width: 340px;
    list-style: none; color: var(--white);
    font-size: 13px; line-height: 16px; font-weight: 700;
  }
  .questions li { padding-left: 10px; text-indent: -6px; margin-bottom: 16px; }
  .questions li::before { content: "•"; font-weight: 400; margin-right: 3px; }

  .quote {
    position: absolute; left: 888px; top: 97px;
    width: 206px; height: 101px;
    background: var(--brand-blue-deep);
    padding: 12px 18px 0 20px;
    color: var(--white); font-size: 13px; line-height: 16px;
  }
  .quote-tail { position: absolute; left: 1014px; top: 196px; }
  .quote-author {
    position: absolute; left: 888px; top: 207px; width: 238px;
    text-align: center; color: var(--white);
    font-size: 15px; font-weight: 700;
  }

  .values {
    position: absolute; right: 42px; top: 310px;
    text-align: right; color: var(--watermark);
    font-size: 39px; line-height: 46px; font-weight: 700;
  }

  .photo {
    position: absolute; left: 376px; top: 486px;
    width: 756px; height: 314px;
    background: linear-gradient(90deg, #d9d9d9 0%, #bdbdbd 45%, #2a2a2a 62%, #1a1a1a 80%, #bfbfbf 100%);
  }
</style>
</head>
<body>
  <div class="spread">
    <div class="rule rule--vertical"></div>
    <div class="rule rule--horizontal"></div>

    <section class="panel panel--what">
      <h2 class="heading heading--lg" style="top:72px;">WHAT WE DO</h2>
      <p class="body-copy" style="top:116px;">Our Approach is to simplify your financial situation, to make it understandable and manageable over the long term.</p>
      <div class="brand-mark"><span class="square"></span><span>Larkmoor Financial Planning SA</span></div>
      <h2 class="heading heading--md" style="top:300px;">OUR SERVICE TO YOU</h2>
      <ul class="body-copy bullet-list" style="top:331px;">
        <li>Different service packages<br>tailored to your needs</li>
        <li>Options to have fees withdrawn<br>from your investments</li>
        <li>We not only set goals, we monitor<br>and review your investments</li>
        <li>Hourly rate work offered</li>
      </ul>
    </section>

    <section class="panel panel--help">
      <h2 class="heading heading--md" style="top:72px;">WE CAN HELP YOU</h2>
      <ul class="body-copy bullet-list" style="top:101px;">
        <li>Save and accumulate wealth</li>
        <li>Protect your wealth</li>
        <li>Protect your family’s wealth</li>
        <li>Transition from work to retirement</li>
        <li>Maximise your retirement income</li>
        <li>With complex Statelink situations<br>and pension claims</li>
        <li>Manage the cost of Aged Care</li>
      </ul>
      <p class="tagline">And if we can’t help you,<br>we can tell you who can.</p>
    </section>

    <ul class="questions">
      <li>Are you looking for saving and investment<br>advice to accumulate wealth?</li>
      <li>Are you ready to retire, or concerned<br>that you may not have enough in your<br>retirement savings?</li>
      <li>Have you recently sold a<br>business or farm property?</li>
      <li>Are you concerned about your<br>capacity to protect your wealth?</li>
      <li>Are you confident that your Estate<br>will be distributed to your beneficiaries<br>in accordance with your wishes?</li>
      <li>Do you need help with your<br>Statelink Age Pension claim?</li>
      <li>Are you or a family member needing<br>Aged Care and are worried about the costs?</li>
    </ul>

    <blockquote class="quote">“We love working with clients who are seeking quality financial advice, and are keen to partner with us to achieve their goals.”</blockquote>
    <svg class="quote-tail" width="40" height="24" viewBox="0 0 40 24" aria-hidden="true">
      <path d="M14 0 H40 C36 14 22 22 0 22 C12 18 15 10 14 0 Z" fill="var(--brand-blue-deep)"/>
    </svg>
    <p class="quote-author">Alex Marlow</p>

    <p class="values">“Certainty”<br>“Direction”<br>“Peace of mind”</p>

    <div class="photo" role="img" aria-label="Black and white photo of a businessman in a suit offering a handshake in front of a city skyline"></div>
  </div>
</body>
</html>
```